West Halvern Commuter Coordination Association Needs an Ad Showcasing 2012's Accomplishments

The West Halvern Commuter Coordination Association is a nonprofit organization with the mission to foster transportation behaviors that benefit the community through advocacy, programs, education, and services. We have had a great year in 2012 and would like to show the community what we have accomplished.

We would like a FULL PAGE ad that will be used in a color print magazine and a black and white print publication.

The Pebble Tram - Over 75,000 trips taken by shuttle riders, a 120% increase in trips over 2011.

Stride Along Program - During the 2011-2012 school year an average of 897 students walked to school weekly on walk to school days.

Pedal Through Spring - 41,950 miles were ridden by students and teachers in May 2012 in 9 participating schools.

Wheel Fixer - over 600 bikes have been serviced in 2012.

Requirements
Must have
• Contact info:
West Halvern CCA
4127 Corliss Rd
Sacramento, CA 95712
916-302-7718
WHCCA.org

Twitter @West HalvernCCA
Facebook.com/WestHalvernCCA

LOGO

```html
<!DOCTYPE html>
<html lang="en">
<head>
<meta charset="utf-8">
<title>West Halvern CCA – 2012 Accomplishments</title>
<link rel="stylesheet" href="https://fonts.googleapis.com/css2?family=Source+Sans+3:wght@600;700&display=swap">
<style>
  :root {
    --backdrop: #3a3a3a;
    --lime: #a6c600;
    --orange: #f28c00;
    --blue: #2a66b8;
    --paper: #ffffff;
    --ink: #4a4a4d;
    --tick-light: #ffd66b;
    --tick-dark: #f0a21a;
  }
  * { box-sizing: border-box; margin: 0; padding: 0; }
  html, body {
    width: 1200px; height: 907px; overflow: hidden;
    background: var(--backdrop);
    font-family: "Source Sans 3", "Myriad Pro", sans-serif;
  }
  .ad-page {
    position: absolute; left: 300px; top: 42px;
    width: 600px; height: 824px;
    overflow: hidden;
  }
  .ad-backdrop { position: absolute; inset: 0; }
  .brand-seal {
    position: absolute; left: 228px; top: 45px;
    width: 144px; height: 144px; border-radius: 50%;
    background: var(--paper);
    border: 4px solid var(--blue);
    display: flex; align-items: center; justify-content: center;
    text-align: center;
  }
  .brand-name {
    font-weight: 700; font-size: 19px; line-height: 1.1;
    color: var(--blue);
  }
  .stat {
    position: absolute; left: 68px; width: 500px;
  }
  .stat-title {
    position: relative;
    padding-left: 37px;
    font-size: 26px; line-height: 30px; font-weight: 700;
    color: var(--lime);
    letter-spacing: -0.2px;
  }
  .stat-title svg {
    position: absolute; left: -6px; top: -8px; width: 40px; height: 34px;
  }
  .stat-body {
    font-size: 20.5px; line-height: 26px; font-weight: 700;
    color: var(--ink);
    margin-top: 3px;
  }
  .stat--tram { top: 229px; }
  .stat--stride { top: 344px; }
  .stat--pedal { top: 485px; }
  .stat--fixer { top: 598px; }
  .contact {
    position: absolute; left: 0; right: 0; top: 776px;
    text-align: center; color: var(--paper);
    font-size: 11px; line-height: 14px; font-weight: 600;
  }
  .contact-name { font-weight: 700; }
</style>
</head>
<body>
<main class="ad-page">
  <svg class="ad-backdrop" viewBox="0 0 600 824" width="600" height="824" aria-hidden="true">
    <defs>
      <linearGradient id="tickFill" x1="0" y1="0" x2="1" y2="1">
        <stop offset="0" stop-color="var(--tick-light)"/>
        <stop offset="1" stop-color="var(--tick-dark)"/>
      </linearGradient>
    </defs>
    <rect width="600" height="420" fill="var(--lime)"/>
    <rect y="420" width="600" height="404" fill="var(--orange)"/>
    <path d="M0,182 Q300,76 600,182 L600,680 Q300,814 0,680 Z" fill="var(--paper)"/>
    <path d="M0,182 Q300,76 600,182" fill="none" stroke="var(--blue)" stroke-width="3"/>
    <path d="M0,187 Q300,81 600,187" fill="none" stroke="var(--orange)" stroke-width="2"/>
    <path d="M0,676 Q300,810 600,676" fill="none" stroke="var(--lime)" stroke-width="2"/>
    <path d="M0,681 Q300,815 600,681" fill="none" stroke="var(--blue)" stroke-width="3"/>
  </svg>

  <div class="brand-seal">
    <span class="brand-name">West Halvern<br>CCA</span>
  </div>

  <section class="stat stat--tram">
    <h2 class="stat-title"><svg viewBox="0 0 40 34" aria-hidden="true"><path d="M3,20 L9,15 L15,22 L34,3 L38,7 L15,31 Z" fill="url(#tickFill)" stroke="#d98a10" stroke-width="1.2"/></svg>The Pebble Tram</h2>
    <p class="stat-body">Over 75,000 trips taken by shuttle riders,<br>a 120% increase in trips over 2011</p>
  </section>

  <section class="stat stat--stride">
    <h2 class="stat-title"><svg viewBox="0 0 40 34" aria-hidden="true"><path d="M3,20 L9,15 L15,22 L34,3 L38,7 L15,31 Z" fill="url(#tickFill)" stroke="#d98a10" stroke-width="1.2"/></svg>Stride Along Program</h2>
    <p class="stat-body">During the 2011-2012 school year an average of<br>897 students walked to school weekly on walk<br>to school days</p>
  </section>

  <section class="stat stat--pedal">
    <h2 class="stat-title"><svg viewBox="0 0 40 34" aria-hidden="true"><path d="M3,20 L9,15 L15,22 L34,3 L38,7 L15,31 Z" fill="url(#tickFill)" stroke="#d98a10" stroke-width="1.2"/></svg>Pedal Through Spring</h2>
    <p class="stat-body">41,950 miles were ridden by students and teach-<br>ers in May 2012 in 9 participating schools.</p>
  </section>

  <section class="stat stat--fixer">
    <h2 class="stat-title"><svg viewBox="0 0 40 34" aria-hidden="true"><path d="M3,20 L9,15 L15,22 L34,3 L38,7 L15,31 Z" fill="url(#tickFill)" stroke="#d98a10" stroke-width="1.2"/></svg>Wheel Fixer</h2>
    <p class="stat-body">Over 600 bikes have been serviced in 2012</p>
  </section>

  <footer class="contact">
    <p class="contact-name">West Halvern CCA</p>
    <p>4127 Corliss Rd; Sacramento, CA 95712; 916-302-7718</p>
    <p>WHCCA.org</p>
  </footer>
</main>
</body>
</html>
```